New concept travel "Fun" for young people !
----- Google Translate ----
With our skills, our agency was the first to develop spring break concepts in French-speaking Belgium by bringing together hundreds of students in Spain to celebrate!
Following a concern for health, our usual graphic designer can not take care of our achievements.
We are looking for a person in the long term (= serious work, contact exchanges and other "contracts").
We will also need a facebook cover and a single-sided A4 poster.
The name of the concept is GOLDEN DRIFT.
You will be free to create a beautiful new logo of course.
This one could possibly be put on future t-shirts for our staff of animators during the trip or offered to the public!
Here is the job to do:
- Objective NEW CONCEPT 2018 in Bulgaria -
We need a visual (efficient and dynamic flyer to attract a population between 21 and 35 years old.
Flyer idea: A6 landscape postcard format, vintage, with a beautiful visual on the front that makes you want and arouse curiosity (with title of the trip "GOLDEN DRIFT - Bulgaria 2018") and the mention "New Concept" with our logo MORELKA TRAVEL .
On the back, on the left half of the postcard: a sweet little word from a woman, the style "Hey ! Le soleil est bien là, les cocktails sont savoureux et l'ambiance incroyable ! On t'attends avec les filles ! Je t'embrasse. Nora" with a fake kiss (= smack).
On the right half, useful information to stay to know:
- du samedi 1 au samedi 8 septembre 2018
- Plage Morvane, Bulgarie
- Voyage "tout compris" : vol aller-retour, hôtel 4**** formule ALL INCLUSIVE, entrées en boites, cocktails offerts, beach party, ... & bien plus !
- prix : € 599,00 par personne en chambre double
- plus d'infos sur www.golden-drift.example ou au 0487 612 940
Here is the logo of our agency + some visuals of our last trip to Hungary (just to give you a little effect to feel ATTENTION I want something else here not copy please, please)
Good luck to everyone !

```html
<!DOCTYPE html>
<html lang="fr">
<head>
<meta charset="utf-8">
<title>Golden Drift – Bulgarie 2018 – carte postale</title>
<link rel="stylesheet" href="https://fonts.googleapis.com/css2?family=Old+Standard+TT:wght@700&family=Dancing+Script:wght@500&display=swap">
<style>
  :root{
    --paper:#ffffff;
    --orange:#f07f1e;
    --sun:#f6c81c;
    --band:#fbe24a;
    --sky:#4db6e6;
    --ink:#8a3a1c;
    --script:#b2472a;
    --stamp:#f3e7d6;
    --stamp-edge:#e9d8bf;
    --stamp-frame:#b07c55;
    --blush:#fcefea;
    --lips:#e88aa6;
    --badge:#efe4cf;
  }
  *{margin:0;padding:0;box-sizing:border-box}
  html,body{width:1200px;height:851px;overflow:hidden;background:var(--paper)}
  .postcard{position:relative;width:1200px;height:851px;background:var(--paper);overflow:hidden;
    font-family:"Old Standard TT",Georgia,serif}
  .edge-left{position:absolute;left:0;top:0;width:14px;height:840px;background:var(--orange)}
  .edge-right-sky{position:absolute;right:10px;top:0;width:5px;height:851px;background:var(--sky)}
  .edge-right-sun{position:absolute;right:0;top:0;width:6px;height:851px;background:var(--sun)}
  .map-area{position:absolute;left:118px;top:96px;width:620px;height:530px;background:var(--blush);
    border-radius:46% 38% 42% 30% / 30% 44% 36% 50%;transform:rotate(-6deg)}
  .dates{position:absolute;left:380px;top:12px;width:420px;text-align:center;color:var(--sun);
    font-size:34px;line-height:50px;font-weight:700;z-index:2}
  .message{position:absolute;left:108px;top:128px;font-family:"Dancing Script",cursive;color:var(--script);
    font-size:27px;line-height:54px;z-index:2}
  .message p{margin:0}
  .message .gap{height:108px}
  .signature{position:absolute;left:322px;top:582px;font-family:"Dancing Script",cursive;color:var(--script);font-size:28px;z-index:2}
  .kiss{position:absolute;left:40px;top:656px;width:132px;height:88px;border-radius:50%;
    background:radial-gradient(ellipse at center,var(--lips) 0%,rgba(232,138,166,.35) 55%,rgba(255,255,255,0) 72%)}
  .divider{position:absolute;left:698px;top:300px;width:4px;height:390px;background:var(--sky)}
  .stamp svg{position:absolute;left:0;top:0}
  .stamp-place{position:absolute;left:728px;top:34px;width:196px;height:168px;transform:rotate(2deg);z-index:3}
  .stamp-place .label{position:absolute;inset:0;display:flex;flex-direction:column;justify-content:center;
    align-items:center;color:var(--ink);font-size:24px;line-height:34px;font-weight:700;text-align:center}
  .stamp-portrait{position:absolute;left:1036px;top:8px;width:128px;height:124px}
  .portrait-fill{position:absolute;left:24px;top:22px;width:80px;height:80px;border-radius:50%;
    background:radial-gradient(circle,#fff 30%,#fde3cf 70%)}
  .triangle-new{position:absolute;left:500px;top:300px;width:290px;height:190px;z-index:3}
  .triangle-new .label{position:absolute;left:90px;top:68px;transform:rotate(-24deg);color:var(--orange);
    font-size:24px;line-height:26px;font-weight:700;text-align:center;-webkit-text-stroke:.6px var(--ink)}
  .all-inclusive{position:absolute;left:786px;top:262px;transform:rotate(-16deg);transform-origin:left bottom;
    color:var(--orange);font-size:44px;font-weight:700;letter-spacing:1px;white-space:nowrap;z-index:4}
  .stamp-offer{position:absolute;left:848px;top:296px;width:330px;height:340px;transform:rotate(-3deg);z-index:3}
  .offer-list{position:absolute;left:30px;top:46px;list-style:none;color:var(--ink);font-size:23px;
    line-height:36px;font-weight:700}
  .offer-more{position:absolute;left:92px;top:252px;color:var(--ink);font-size:23px;font-weight:700}
  .price{position:absolute;left:624px;top:574px;width:190px;height:140px;z-index:3}
  .price .amount{position:absolute;left:60px;top:62px;transform:rotate(-28deg);color:var(--orange);
    font-size:24px;font-weight:700;-webkit-text-stroke:.5px var(--ink)}
  .price-note{position:absolute;left:640px;top:738px;transform:rotate(-9deg);color:var(--script);
    font-size:13px;font-weight:700;white-space:nowrap;z-index:3}
  .guarantee{position:absolute;left:950px;top:636px;width:190px;height:190px;border-radius:50%;
    border:10px solid var(--badge);background:#f8f2e6;opacity:.9}
  .contact-band{position:absolute;left:240px;top:800px;width:720px;height:46px;background:var(--band);
    display:flex;align-items:center;justify-content:center;color:var(--script);font-size:23px;font-weight:700}
</style>
</head>
<body>
<main class="postcard">
  <div class="edge-left"></div>
  <div class="edge-right-sky"></div>
  <div class="edge-right-sun"></div>

  <div class="map-area" role="img" aria-label="Carte stylisée de la Bulgarie en rose pâle"></div>

  <div class="dates">du sam 1 au sam8<br>septembre 2018</div>

  <div class="message">
    <p>"Hey ! Le soleil est bien là,</p>
    <p>les cocktails sont savoureux et l'ambiance incroyable !</p>
    <p>On t'attends avec les filles !</p>
    <div class="gap"></div>
    <p>Je t'embrasse.</p>
  </div>
  <div class="signature">Nora</div>
  <div class="kiss" role="img" aria-label="Trace de baiser au rouge à lèvres"></div>

  <div class="stamp stamp-place">
    <svg width="196" height="168" viewBox="0 0 196 168">
      <rect x="6" y="6" width="184" height="156" fill="var(--stamp)"/>
      <rect x="6" y="6" width="184" height="156" fill="none" stroke="var(--paper)" stroke-width="9" stroke-linecap="round" stroke-dasharray="0 13"/>
      <rect x="22" y="22" width="152" height="124" fill="var(--stamp-edge)" stroke="var(--stamp-frame)" stroke-width="1.5" opacity=".7"/>
    </svg>
    <div class="label"><span>Plage Morvane</span><span>Bulgarie</span></div>
  </div>

  <div class="stamp stamp-portrait">
    <svg width="128" height="124" viewBox="0 0 128 124">
      <rect x="5" y="5" width="118" height="114" fill="var(--orange)"/>
      <rect x="5" y="5" width="118" height="114" fill="none" stroke="var(--paper)" stroke-width="7" stroke-linecap="round" stroke-dasharray="0 11"/>
      <rect x="18" y="16" width="92" height="92" fill="none" stroke="var(--paper)" stroke-width="3"/>
    </svg>
    <div class="portrait-fill" role="img" aria-label="Illustration vintage d'un portrait de femme sur un timbre"></div>
  </div>

  <div class="divider"></div>

  <div class="stamp triangle-new">
    <svg width="290" height="190" viewBox="0 0 290 190">
      <polygon points="14,110 230,14 268,176" fill="var(--stamp)"/>
      <polygon points="14,110 230,14 268,176" fill="none" stroke="var(--stamp-frame)" stroke-width="9" stroke-linecap="round" stroke-dasharray="0 13" opacity=".8"/>
      <polygon points="46,110 218,36 248,160" fill="none" stroke="var(--stamp-frame)" stroke-width="1.5"/>
    </svg>
    <div class="label">NEW<br>CONCEPT</div>
  </div>

  <div class="stamp stamp-offer">
    <svg width="330" height="340" viewBox="0 0 330 340">
      <rect x="6" y="6" width="318" height="328" fill="var(--stamp)"/>
      <rect x="6" y="6" width="318" height="328" fill="none" stroke="var(--stamp-frame)" stroke-width="10" stroke-linecap="round" stroke-dasharray="0 15" opacity=".8"/>
      <rect x="22" y="22" width="286" height="296" fill="none" stroke="var(--stamp-frame)" stroke-width="1.5"/>
    </svg>
    <ul class="offer-list">
      <li>vol aller-retour</li>
      <li>hôtel 4****</li>
      <li>entrées en boites</li>
      <li>cocktails offerts</li>
      <li>beach party, ...</li>
    </ul>
    <div class="offer-more">&amp; bien plus !</div>
  </div>
  <div class="all-inclusive">ALL INCLUSIVE</div>

  <div class="stamp price">
    <svg width="190" height="140" viewBox="0 0 190 140">
      <polygon points="10,128 150,8 182,120" fill="var(--stamp)"/>
      <polygon points="10,128 150,8 182,120" fill="none" stroke="var(--stamp-frame)" stroke-width="8" stroke-linecap="round" stroke-dasharray="0 12" opacity=".8"/>
      <polygon points="34,122 148,28 172,114" fill="var(--sun)"/>
    </svg>
    <div class="amount">599.00€</div>
  </div>
  <div class="price-note">par personne en chambre double</div>

  <div class="guarantee" aria-hidden="true"></div>

  <div class="contact-band">www.golden-drift.example ou au 0487 612 940</div>
</main>
</body>
</html>
```